mosswickpartners Business Card Design

Business card with logo design for mosswickpartners. We are a group of professional project managers based on the Pareto Principle that 80% of the work is done by 20% of the people. I have a makeshift logo that uses a pi chart with 30% and 20% and the 20% pie slice is set slightly out and up. Have played around with a teal and orange colour scheme.

Industry/Entity Type

Business

Contact Information for Business Card

Harold Penbury
Director
mosswickpartners

0487 263019

```html
<!DOCTYPE html>
<html lang="en">
<head>
<meta charset="utf-8">
<title>mosswickpartners Business Card</title>
<link rel="stylesheet" href="https://fonts.googleapis.com/css2?family=Questrial&display=swap">
<style>
  :root {
    --backdrop: #e4e4e6;
    --paper: #ffffff;
    --orange: #f0955c;
    --teal: #2b8e9a;
    --teal-text: #2a8a97;
    --rule: #f0f3f3;
    --white: #ffffff;
  }
  * { margin: 0; padding: 0; box-sizing: border-box; }
  html, body {
    width: 1200px; height: 1000px; overflow: hidden;
    background: var(--backdrop);
    font-family: "Questrial", sans-serif;
  }
  .canvas { position: relative; width: 1200px; height: 1000px; }
  .card {
    position: absolute; background: var(--paper); overflow: hidden;
    box-shadow: 0 1px 3px rgba(0,0,0,0.12);
  }

  /* Front */
  .card-front { left: 28px; top: 22px; width: 434px; height: 261px; }
  .brand {
    position: absolute; left: 0; right: 0; display: flex;
    align-items: center; justify-content: center; gap: 6px;
    color: var(--teal-text); letter-spacing: 0.3px;
  }
  .brand-dot { border-radius: 50%; background: var(--orange); }
  .card-front .brand { top: 52px; font-size: 15px; }
  .card-front .brand-dot { width: 22px; height: 22px; }
  .detail-row { position: absolute; left: 0; right: 0; height: 16px; }
  .detail-row .rule { position: absolute; top: 3px; height: 11px; background: var(--rule); }
  .detail-row .label {
    position: absolute; left: 0; right: 0; text-align: center;
    font-size: 11px; line-height: 16px; color: var(--teal-text);
  }
  .row-name { top: 111px; } .row-name .rule { left: 0; width: 164px; }
  .row-title { top: 136px; } .row-title .rule { left: 247px; right: 0; }
  .row-company { top: 161px; } .row-company .rule { left: 0; width: 164px; }
  .contact-band {
    position: absolute; left: 0; right: 0; top: 190px; bottom: 0;
    background: var(--orange);
  }
  .contact-band .notch { position: absolute; left: 208px; top: 0; }
  .contact-line {
    position: absolute; left: 0; right: 0; display: flex; justify-content: center;
    align-items: center; gap: 6px; color: var(--white); font-size: 9px;
  }
  .contact-phone { top: 25px; }
  .contact-web { top: 49px; }
  .contact-line svg { opacity: 0.8; }

  /* Back */
  .card-back { left: 28px; top: 715px; width: 440px; height: 265px; }
  .band { position: absolute; left: 0; right: 0; background: var(--teal); }
  .band-top { top: 0; height: 27px; }
  .band-bottom { bottom: 0; height: 29px; display: flex; align-items: center;
    justify-content: center; color: var(--white); font-size: 9px; }
  .card-back .brand { top: 118px; font-size: 16px; }
  .card-back .brand-dot { width: 24px; height: 24px; }
</style>
</head>
<body>
<main class="canvas">
  <section class="card card-front">
    <div class="brand"><span class="brand-dot"></span><span>mosswickpartners</span></div>
    <div class="detail-row row-name"><span class="rule"></span><p class="label">Harold Penbury</p></div>
    <div class="detail-row row-title"><span class="rule"></span><p class="label">Director</p></div>
    <div class="detail-row row-company"><span class="rule"></span><p class="label">mosswickpartners</p></div>
    <div class="contact-band">
      <svg class="notch" width="18" height="10" viewBox="0 0 18 10"><polygon points="0,0 18,0 9,10" fill="#ffffff"/></svg>
      <p class="contact-line contact-phone">
        <svg width="9" height="9" viewBox="0 0 10 10"><rect x="0.5" y="0.5" width="9" height="9" rx="1.5" fill="none" stroke="#fff"/><path d="M3 2.5 L4.2 2.5 L4.6 4 L3.9 4.5 Q4.6 6 5.8 6.4 L6.3 5.7 L7.6 6.2 L7.6 7.4 Q4 7.6 2.6 3.6 Z" fill="#fff"/></svg>
        <span>0487 263019</span>
      </p>
      <p class="contact-line contact-web">
        <svg width="9" height="9" viewBox="0 0 10 10"><circle cx="5" cy="5" r="4.3" fill="none" stroke="#fff"/><ellipse cx="5" cy="5" rx="1.8" ry="4.3" fill="none" stroke="#fff" stroke-width="0.7"/><line x1="0.7" y1="5" x2="9.3" y2="5" stroke="#fff" stroke-width="0.7"/></svg>
        <span>www.mosswickpartners.com.au</span>
      </p>
    </div>
  </section>

  <section class="card card-back">
    <div class="band band-top"></div>
    <div class="brand"><span class="brand-dot"></span><span>mosswickpartners</span></div>
    <div class="band band-bottom">www.mosswickpartners.com.au</div>
  </section>
</main>
</body>
</html>
```